Simple proffessional BC

I have a logo which I will attach below.
I would like the logo on the front of the card with these details in point form below:
Pre and Post Natal Yoga: Pregnancy Workshops: Hypnobirthing Courses
On the back of the card my details:
Merrin Galvey
Facebook page- calmbellieswillowharbour
Mobile- 0438 512 740

I like the idea of the card being simple, possibly just the above on a plain coloured (eggshell?) card, a card that is textured.
I am open to suggestion if it appeals!
Thank you and good luck!

Target Market(s)

Pregnant women, 20's-40's

Requirements
Must have
• Simple, compliment logo.
Make logo the feature.
Should not have

• .

```html
<!DOCTYPE html>
<html lang="en">
<head>
<meta charset="utf-8">
<title>Calm Bellies – Business Card</title>
<link href="https://fonts.googleapis.com/css2?family=Noto+Sans+Mono:wght@400&display=swap" rel="stylesheet">
<style>
  :root {
    --backdrop: #2a2a2a;
    --maroon: #7e1a1c;
    --saffron: #e9a53b;
    --saffron-deep: #e29b30;
    --paper: #f4f4f2;
    --card-w: 800px;
    --card-h: 457px;
  }
  * { box-sizing: border-box; margin: 0; padding: 0; }
  html, body {
    width: 1037px;
    height: 1200px;
    overflow: hidden;
    background: var(--backdrop);
  }
  .sheet {
    width: 1037px;
    height: 1200px;
    display: flex;
    flex-direction: column;
    align-items: center;
    justify-content: center;
    gap: 90px;
  }
  .card {
    position: relative;
    width: var(--card-w);
    height: var(--card-h);
    overflow: hidden;
    font-family: "Noto Sans Mono", monospace;
    box-shadow: 0 14px 30px rgba(0,0,0,0.45);
  }
  .card svg { position: absolute; inset: 0; display: block; }

  /* Details side */
  .card--details { background: var(--maroon); }
  .details__name {
    position: absolute;
    left: 40px;
    top: 56px;
    color: var(--saffron);
    font-size: 27px;
    letter-spacing: 4px;
  }
  .details__contact {
    position: absolute;
    left: 40px;
    bottom: 30px;
    color: var(--saffron);
  }
  .details__phone {
    font-size: 29px;
    letter-spacing: 4px;
    line-height: 1.1;
  }
  .details__page {
    font-size: 15px;
    letter-spacing: 2px;
  }
  .details__brand {
    position: absolute;
    left: 520px;
    top: 234px;
    transform: translate(-50%, -50%);
    color: var(--maroon);
    font-size: 26px;
    white-space: nowrap;
  }

  /* Brand side */
  .card--brand {
    background: linear-gradient(180deg, var(--saffron) 0%, var(--saffron-deep) 100%);
  }
  .brand__name {
    position: absolute;
    left: 0;
    right: 0;
    top: 262px;
    text-align: center;
    color: var(--maroon);
    font-size: 60px;
    line-height: 1;
    letter-spacing: 2px;
  }
  .brand__services {
    position: absolute;
    left: 0;
    right: 0;
    top: 372px;
    display: flex;
    justify-content: center;
    gap: 30px;
    list-style: none;
    color: var(--maroon);
    font-size: 15px;
    letter-spacing: 0.5px;
    white-space: nowrap;
  }
  .brand__services li::before {
    content: "•";
    margin-right: 8px;
  }
</style>
</head>
<body>
<main class="sheet">

  <section class="card card--details" aria-label="Card back with contact details">
    <svg viewBox="0 0 800 457" width="800" height="457" aria-hidden="true">
      <path d="M505 0 C330 60 270 300 395 457 L800 457 L800 0 Z" fill="var(--paper)"/>
      <circle cx="520" cy="234" r="122" fill="var(--saffron)"/>
    </svg>
    <p class="details__name">Merrin Galvey</p>
    <span class="details__brand">Calm Bellies</span>
    <div class="details__contact">
      <p class="details__phone">0438 512 740</p>
      <p class="details__page">calmbellieswillowharbour</p>
    </div>
  </section>

  <section class="card card--brand" aria-label="Card front with brand name and services">
    <svg viewBox="0 0 800 457" width="800" height="457" aria-hidden="true">
      <circle cx="400" cy="128" r="100" fill="none" stroke="#ffffff" stroke-width="13"/>
    </svg>
    <p class="brand__name">Calm Bellies</p>
    <ul class="brand__services">
      <li>Pre and Post Natal Yoga</li>
      <li>Pregnancy Workshops</li>
      <li>Hypnobirthing Courses</li>
    </ul>
  </section>

</main>
</body>
</html>
```